'SOLVANO' NEW WINE LABEL DESIGN

I am looking for an exceptional and exciting design for a wine label called 'Solvano' meaning 'Lookout'. The design must feature the name 'Solvano', and the word 'Cabernet Sauvignon' in version 1 and 'Sauvignon Blanc' in version 2. It will also need the words 'Valle Central, Chile' at the bottom of the label as a prominent piece of information as well as the vintage 2017. Please produce the work in size 80mm x 100mm. Feel free to use colour in addition to black/white and ensue that the label is easy to read on a shelf placement.
Low design quality
Target Market(s)
SUPERMARKETS & WINE STORES
Requirements
Must have
- EASY TO READ, USE COLOURS LIKE GREEN FOR SAUVIGNON & RED FOR CABERNET SAUVIGNON
- FULL BOTTLE SHOT MUST BE IN PROVIDED DESIGNS. ALL BOTTLE TOPS SHOULD BE VENDRAX STYLE (SCREW TOP)
- PLEASE NOTE THAT LABEL INFORMATION MUSY BE EASY TO READ I.E. VINTAGE, PLACE OF ORGIN ALTHOUGH NOT THE MAIN CONTENT MUST STILL BE CLEAR.
Nice to have
- ARTISTIC REFERENCE LINK TO NAME & ANDES BUT NOT PICTURES OF MOUNTAINS
Should not have
- PICTURES OF GRAPES
- PICTURES OF VINEYARDS
- PICTURES OF MOUNTAINS

```html
<!DOCTYPE html>
<html lang="en">
<head>
<meta charset="utf-8">
<title>Solvano Sauvignon Blanc – Wine Label</title>
<link href="https://fonts.googleapis.com/css2?family=Cormorant+Garamond:wght@500;600&family=Pinyon+Script&display=swap" rel="stylesheet">
<style>
  :root {
    --page: #ffffff;
    --label-paper: #ebebe9;
    --ink: #1f1f1f;
    --gold: #8a6a3a;
    --rule: #c4b79f;
    --wash-pale: #e3ecb4;
    --wash-light: #c3dc7c;
    --wash-mid: #8cc263;
    --wash-deep: #4a9d78;
    --earth: #4a3a2a;
  }
  * { margin: 0; padding: 0; box-sizing: border-box; }
  html, body {
    width: 1200px;
    height: 1200px;
    overflow: hidden;
    background: var(--page);
  }
  .canvas {
    position: relative;
    width: 1200px;
    height: 1200px;
  }
  .wine-label {
    position: absolute;
    left: 220px;
    top: 125px;
    width: 760px;
    height: 950px;
    background: var(--label-paper);
    text-align: center;
    color: var(--ink);
    overflow: hidden;
  }
  .landscape-art {
    position: absolute;
    left: 130px;
    top: 165px;
    width: 630px;
    height: 200px;
    background: linear-gradient(90deg,
      rgba(227,236,180,0) 0%,
      var(--wash-pale) 14%,
      var(--wash-light) 38%,
      var(--wash-mid) 60%,
      var(--wash-deep) 80%,
      var(--earth) 100%);
    -webkit-mask-image: linear-gradient(180deg, transparent 0%, #000 30%, #000 72%, transparent 100%);
    mask-image: linear-gradient(180deg, transparent 0%, #000 30%, #000 72%, transparent 100%);
    opacity: 0.9;
  }
  .brand-name {
    position: absolute;
    top: 400px;
    left: 0;
    width: 100%;
    font-family: "Cormorant Garamond", serif;
    font-weight: 600;
    font-size: 96px;
    letter-spacing: 7px;
    line-height: 1;
  }
  .divider {
    position: absolute;
    top: 522px;
    left: 340px;
    width: 80px;
    height: 1px;
    background: var(--rule);
  }
  .varietal {
    position: absolute;
    top: 550px;
    left: 0;
    width: 100%;
    font-family: "Cormorant Garamond", serif;
    font-weight: 600;
    font-size: 28px;
    line-height: 1;
    font-variant: small-caps;
    letter-spacing: 4px;
    color: var(--gold);
  }
  .region {
    position: absolute;
    top: 590px;
    left: 0;
    width: 100%;
    font-family: "Pinyon Script", cursive;
    font-size: 40px;
    line-height: 1.1;
  }
  .vintage {
    position: absolute;
    top: 652px;
    left: 0;
    width: 100%;
    font-family: "Cormorant Garamond", serif;
    font-weight: 600;
    font-size: 24px;
    line-height: 1;
    letter-spacing: 5px;
    color: var(--earth);
  }
</style>
</head>
<body>
  <main class="canvas">
    <section class="wine-label">
      <div class="landscape-art" role="img" aria-label="Watercolour landscape wash in soft greens fading into a dark brushstroke at the right edge"></div>
      <h1 class="brand-name">SOLVANO</h1>
      <div class="divider"></div>
      <p class="varietal">Sauvignon Blanc</p>
      <p class="region">Valle Central, Chile</p>
      <p class="vintage">2017</p>
    </section>
  </main>
</body>
</html>
```